Business Card Upgrade

I have designed our business card using our new logo. I think it needs imporovements. We used to have two cards for our business. One card was for our software business, and the other was for our consulting business. We are now in the process of combining our websites, marketing, name, and a new logo.

Our goal is to have a really sharp professional logo. One reason I designed the card the way I did was that our Titles are sometimes long, and by separating the person's name and title, it shows up very well and the title can be adjusted no matter how long it is. Sometimes the title can be 4 or 5 words or more.

We really like our logo on black as it shows up very nice. Our PMS colors are as follows: 368C and 459C.

The Designer that will be working with us will need to deliver the following:

The front and back of the Business Card Design will need to be delivered in a high quality JPEG, and
The front and back of the Business Card Design in Illustrator Format .ai
Any fonts will need to be sent to us if they are not standard and are required to open the Illustrator file correctly.

To help us get a good idea of the card with a title, please use the title: " Director of Software Development "

NOTE: The chosen designer will be selected to design our new letterhead within 2 weeks from the closing of this contest.
Updates

To help us make sure the card design works with longer titles, please use the followign job title on the card:  

"Director of Software and Product Development"

 

ALL DESIGNERS:

1. I appreciate the different angles you are showing the cards, but please be sure and always show the direct view, so I can see the layout and what the person I hand the card will see.

2. Please do not use white.  Please use off white as I don't care for white cards and they get dirty easy and do not represent the designs well.

Dear Designers,

Please provide samples straight one as a viewer of the card will see.  Some of the angles that are presented make it impossible to tell how everything fits, and sometimes even makes areas look skewed. So, please provide a straight sample view.

Target Market(s)

Keystone 400 company executives such as Vice Presidents, and Directors

Industry/Entity Type

Software

Requirements
Must have
• Professional looking Card.

Our customers are Directors, Vice Presidents, and Presidents of companies as large as Keystone 400 companies. The card needs to get attention wile still looking professional.

Delivery of the finished product in Illustrator Format with any fonts needed to edit the text or open the file.

The card will be a heavy stock with a soft touch coating for that silk feel.

```html
<!DOCTYPE html>
<html lang="en">
<head>
<meta charset="utf-8">
<title>Northgate Trade Corporation — Business Card Options</title>
<link rel="stylesheet" href="https://fonts.googleapis.com/css2?family=Questrial&family=Source+Sans+3:wght@400;600&display=swap">
<style>
  :root {
    --page: #e4e1dc;
    --green: #62ad47;
    --gold: #e6d59c;
    --gold-text: #d9c27a;
    --offwhite: #f6f6f3;
    --ink: #555555;
    --black: #0d0a0a;
    --white: #ffffff;
  }
  * { box-sizing: border-box; margin: 0; padding: 0; }
  html, body { width: 1200px; height: 900px; overflow: hidden; }
  body {
    position: relative;
    background: var(--page);
    font-family: "Source Sans 3", "Myriad Pro", Arial, sans-serif;
  }
  .option-label {
    position: absolute;
    left: 0; width: 1244px;
    text-align: center;
    font-family: "Questrial", "Century Gothic", sans-serif;
    font-size: 30px;
    font-weight: 400;
    letter-spacing: 1px;
    color: #111;
  }
  .option-label--one { top: 58px; }
  .option-label--two { top: 474px; }

  .card {
    position: absolute;
    width: 530px; height: 303px;
    overflow: hidden;
    box-shadow: 0 4px 10px rgba(0,0,0,.35);
  }
  .card--front-light { left: 65px; top: 115px; background: linear-gradient(135deg, var(--white), var(--offwhite) 60%, #ececea); }
  .card--back-green { left: 622px; top: 115px; background: var(--green); }
  .card--front-dark { left: 65px; top: 530px; width: 532px; height: 304px; background: var(--black); }
  .card--back-dark { left: 624px; top: 532px; width: 528px; height: 299px; background: var(--black); }

  .card__band {
    position: absolute;
    left: 0; bottom: 0;
    width: 100%; height: 44px;
    background: linear-gradient(180deg, var(--gold) 0 5px, var(--green) 5px);
  }

  .wordmark {
    position: absolute;
    left: 0; width: 100%;
    text-align: center;
    font-weight: 600;
    font-size: 27px;
    letter-spacing: 2px;
    color: var(--green);
    text-transform: uppercase;
  }
  .wordmark--front { top: 62px; }
  .wordmark--back { top: 132px; font-size: 34px; }
  .card--back-green .wordmark { color: var(--white); }

  .person { position: absolute; left: 33px; top: 136px; }
  .person__name { font-size: 20px; font-weight: 600; color: var(--green); line-height: 22px; text-transform: uppercase; }
  .person__title { font-size: 11px; color: var(--gold-text); margin-top: 2px; }

  .contact { position: absolute; list-style: none; font-size: 13px; line-height: 17px; color: var(--ink); }
  .card--front-dark .contact { color: #e8e8e8; }
  .contact--personal { left: 34px; top: 180px; }
  .contact--office { right: 38px; top: 180px; text-align: right; }
  .contact li { display: flex; align-items: center; gap: 8px; height: 17px; }
  .contact--office li { justify-content: flex-end; }
  .contact--office .contact__plain { padding-right: 20px; }
  .contact svg { width: 12px; height: 12px; fill: var(--green); flex: none; }

  .divider { position: absolute; left: 264px; top: 178px; width: 1px; height: 66px; background: #b9b9b9; }
  .card--front-dark .divider { background: var(--green); }

  .website { position: absolute; left: 0; bottom: 20px; width: 100%; text-align: center; font-size: 13px; color: var(--white); }
  .website__domain { color: var(--green); }

  .halftone {
    position: absolute; inset: 0;
    background:
      radial-gradient(ellipse at 0% 0%, #5a5a5a 0%, rgba(40,40,40,.6) 25%, transparent 45%),
      radial-gradient(ellipse at 100% 100%, #6a6a6a 0%, rgba(40,40,40,.6) 25%, transparent 48%);
  }
</style>
</head>
<body>

  <h2 class="option-label option-label--one">OPTION-1</h2>

  <section class="card card--front-light">
    <div class="card__band" role="img" aria-label="Green and gold band along the bottom edge of the card"></div>
    <div class="wordmark wordmark--front">Northgate Trade</div>
    <div class="person">
      <p class="person__name">Dale Morrow</p>
      <p class="person__title">Director of Software and Product Development</p>
    </div>
    <ul class="contact contact--personal">
      <li><svg viewBox="0 0 12 12"><path d="M2.5 0.5 L4.5 2.8 L3.4 4.2 Q4.5 6.8 7.8 8.6 L9.2 7.5 L11.5 9.5 L10 11.5 Q3 10.5 0.5 2 Z"/></svg>000 0 0000000</li>
      <li><svg viewBox="0 0 12 12"><path d="M3 0 H9 V12 H3 Z M4 1.5 V9.5 H8 V1.5 Z"/></svg>000 0 0000000</li>
      <li><svg viewBox="0 0 12 12"><path d="M0 2 H12 V10 H0 Z M1 3 L6 6.5 L11 3 Z" fill-rule="evenodd"/></svg>name@domainname.com</li>
    </ul>
    <span class="divider"></span>
    <ul class="contact contact--office">
      <li>Your Office Address Goes Here,<svg viewBox="0 0 12 12"><path d="M6 0.5 L12 6 H10 V11.5 H7 V8 H5 V11.5 H2 V6 H0 Z"/></svg></li>
      <li class="contact__plain">City, Zip Code, Country Name</li>
      <li>www.websitename.com<svg viewBox="0 0 12 12"><circle cx="6" cy="6" r="5.8"/></svg></li>
    </ul>
  </section>

  <section class="card card--back-green">
    <div class="wordmark wordmark--back">Northgate Trade</div>
    <p class="website">www.websitename.com</p>
  </section>

  <h2 class="option-label option-label--two">OPTION-2</h2>

  <section class="card card--front-dark">
    <div class="card__band" role="img" aria-label="Green and gold band along the bottom edge of the card"></div>
    <div class="wordmark wordmark--front">Northgate Trade</div>
    <div class="person">
      <p class="person__name">Dale Morrow</p>
      <p class="person__title">Director of Software and Product Development</p>
    </div>
    <ul class="contact contact--personal">
      <li><svg viewBox="0 0 12 12"><path d="M2.5 0.5 L4.5 2.8 L3.4 4.2 Q4.5 6.8 7.8 8.6 L9.2 7.5 L11.5 9.5 L10 11.5 Q3 10.5 0.5 2 Z"/></svg>000 0 0000000</li>
      <li><svg viewBox="0 0 12 12"><path d="M3 0 H9 V12 H3 Z M4 1.5 V9.5 H8 V1.5 Z"/></svg>000 0 0000000</li>
      <li><svg viewBox="0 0 12 12"><path d="M0 2 H12 V10 H0 Z M1 3 L6 6.5 L11 3 Z" fill-rule="evenodd"/></svg>name@domainname.com</li>
    </ul>
    <span class="divider"></span>
    <ul class="contact contact--office">
      <li>Your Office Address Goes Here,<svg viewBox="0 0 12 12"><path d="M6 0.5 L12 6 H10 V11.5 H7 V8 H5 V11.5 H2 V6 H0 Z"/></svg></li>
      <li class="contact__plain">City, Zip Code, Country Name</li>
      <li>www.websitename.com<svg viewBox="0 0 12 12"><circle cx="6" cy="6" r="5.8"/></svg></li>
    </ul>
  </section>

  <section class="card card--back-dark">
    <div class="halftone" role="img" aria-label="Grey halftone dot pattern fading in from the top-left and bottom-right corners"></div>
    <div class="wordmark wordmark--back">Northgate Trade</div>
    <p class="website">www.<span class="website__domain">websitename</span>.com</p>
  </section>

</body>
</html>
```